Design a Happy Birthday Banner

I would like a design of a "HAPPY BIRTHDAY" flag banner/bunting. Each flag is to be a standard size of 15cm width * 17cm tall. This design must be appropriate for use by a Paper Manufacturing factory to use in creating the product. More graphic design work available (e.g. packaging template design/images compilations/logo creation/etc) if I am happy with the resulting work and fees.

Attached is a similar style that I copy and pasted from Google search, this is the type of product I want created.

```html
<!DOCTYPE html>
<html lang="en">
<head>
<meta charset="utf-8">
<title>Happy Birthday Bunting</title>
<link rel="stylesheet" href="https://fonts.googleapis.com/css2?family=Nunito:wght@900&display=swap">
<style>
  :root {
    --page: #ffffff;
    --pink: #ec2a8a;
    --pink-soft: #f562ab;
    --green: #86d62a;
    --green-soft: #aee865;
    --badge: #ffffff;
    --badge-ring: #d9d9d9;
    --letter: #111111;
    --shadow: rgba(0, 0, 0, 0.28);
  }
  html, body {
    margin: 0;
    padding: 0;
    width: 1200px;
    height: 700px;
    overflow: hidden;
    background: var(--page);
  }
  .bunting {
    display: block;
    width: 1200px;
    height: 700px;
  }
  .pennant-shadow { fill: var(--shadow); filter: url(#soft-shadow); }
  .pennant-body--pink { fill: url(#pink-fill); }
  .pennant-body--green { fill: url(#green-fill); }
  .letter-badge { fill: var(--badge); stroke: var(--badge-ring); stroke-width: 1.5; }
  .letter {
    font-family: "Nunito", "Arial Rounded MT Bold", sans-serif;
    font-weight: 900;
    font-size: 36px;
    fill: var(--letter);
    text-anchor: middle;
    dominant-baseline: central;
  }
</style>
</head>
<body>
<svg class="bunting" viewBox="0 0 1200 700" xmlns="http://www.w3.org/2000/svg">
  <defs>
    <filter id="soft-shadow" x="-30%" y="-30%" width="160%" height="160%">
      <feGaussianBlur stdDeviation="6"/>
    </filter>
    <linearGradient id="pink-fill" x1="0" y1="0" x2="1" y2="1">
      <stop offset="0" stop-color="var(--pink-soft)"/>
      <stop offset="1" stop-color="var(--pink)"/>
    </linearGradient>
    <linearGradient id="green-fill" x1="0" y1="0" x2="1" y2="1">
      <stop offset="0" stop-color="var(--green-soft)"/>
      <stop offset="1" stop-color="var(--green)"/>
    </linearGradient>
    <g id="flag-shadow"><polygon class="pennant-shadow" points="-50,14 66,14 14,150"/></g>
    <g id="flag-pink"><polygon class="pennant-body--pink" points="-58,0 58,0 0,131" role="img" aria-label="Pink patterned pennant"/></g>
    <g id="flag-green"><polygon class="pennant-body--green" points="-58,0 58,0 0,131" role="img" aria-label="Green patterned pennant"/></g>
    <circle id="badge" class="letter-badge" cx="0" cy="44" r="28"/>
  </defs>

  <g class="bunting-row bunting-row--happy">
    <g class="pennant" transform="translate(322,187)"><use href="#flag-shadow"/><use href="#flag-pink"/><use href="#badge"/><text class="letter" x="0" y="45">H</text></g>
    <g class="pennant" transform="translate(461,187)"><use href="#flag-shadow"/><use href="#flag-green"/><use href="#badge"/><text class="letter" x="0" y="45">A</text></g>
    <g class="pennant" transform="translate(600,187)"><use href="#flag-shadow"/><use href="#flag-pink"/><use href="#badge"/><text class="letter" x="0" y="45">P</text></g>
    <g class="pennant" transform="translate(739,187)"><use href="#flag-shadow"/><use href="#flag-green"/><use href="#badge"/><text class="letter" x="0" y="45">P</text></g>
    <g class="pennant" transform="translate(878,187)"><use href="#flag-shadow"/><use href="#flag-pink"/><use href="#badge"/><text class="letter" x="0" y="45">Y</text></g>
  </g>

  <g class="bunting-row bunting-row--birthday">
    <g class="pennant" transform="translate(126,400)"><use href="#flag-shadow"/><use href="#flag-green"/><use href="#badge"/><text class="letter" x="0" y="45">B</text></g>
    <g class="pennant" transform="translate(265,400)"><use href="#flag-shadow"/><use href="#flag-pink"/><use href="#badge"/><text class="letter" x="0" y="45">I</text></g>
    <g class="pennant" transform="translate(404,400)"><use href="#flag-shadow"/><use href="#flag-green"/><use href="#badge"/><text class="letter" x="0" y="45">R</text></g>
    <g class="pennant" transform="translate(543,400)"><use href="#flag-shadow"/><use href="#flag-pink"/><use href="#badge"/><text class="letter" x="0" y="45">T</text></g>
    <g class="pennant" transform="translate(682,400)"><use href="#flag-shadow"/><use href="#flag-green"/><use href="#badge"/><text class="letter" x="0" y="45">H</text></g>
    <g class="pennant" transform="translate(821,400)"><use href="#flag-shadow"/><use href="#flag-pink"/><use href="#badge"/><text class="letter" x="0" y="45">D</text></g>
    <g class="pennant" transform="translate(960,400)"><use href="#flag-shadow"/><use href="#flag-green"/><use href="#badge"/><text class="letter" x="0" y="45">A</text></g>
    <g class="pennant" transform="translate(1099,400)"><use href="#flag-shadow"/><use href="#flag-pink"/><use href="#badge"/><text class="letter" x="0" y="45">Y</text></g>
  </g>
</svg>
</body>
</html>
```